Business card for a restaurant/bar

We are looking for a business card design/template for TOMMO Larkdale that can be a starting point for a corporate identity pack. We are known for live bands on the weekends, sports, burgers, beers and American cuisine. We have a relaxing/friendly environment and our tag line is "No Fuss. Just Games, Good Grub, Live Bands And Good Nights." We are located down the street from a college campus and we attract a wide variety of customers from college students, business professionals, and those interested in sports and general trivia.
Visit our website: www.tommolarkdale.example and see the attached files for more info about us.
Please use the current logo.

```html
<!DOCTYPE html>
<html lang="en">
<head>
<meta charset="utf-8">
<title>TOMMO Larkdale – Business Card</title>
<link rel="stylesheet" href="https://fonts.googleapis.com/css2?family=Open+Sans:wght@700;800&family=Tinos:wght@400;700&display=swap">
<style>
  :root {
    --stage: #e4e2df;
    --card-black: #101010;
    --card-black-soft: #1c1c1c;
    --cork: #c9a27a;
    --cork-dark: #9c7650;
    --cork-light: #e0c29c;
    --burger-top: #c88a3e;
    --burger-mid: #7a3a1e;
    --burger-low: #d9a350;
    --white: #ffffff;
    --cab-yellow: #e8e22a;
    --brand-red: #c4161c;
    --muted: #d8d8d8;
  }
  * { margin: 0; padding: 0; box-sizing: border-box; }
  html, body {
    width: 1200px; height: 800px; overflow: hidden;
    background: var(--stage);
  }
  .stage {
    position: relative; width: 1200px; height: 800px;
    display: flex; align-items: center; justify-content: center; gap: 40px;
  }
  .card {
    background: radial-gradient(ellipse at 50% 40%, var(--card-black-soft), var(--card-black) 75%);
    box-shadow: 0 6px 18px rgba(0,0,0,0.25);
    position: relative; overflow: hidden;
  }

  /* Front card: portrait, content set reading bottom-to-top */
  .card--front { width: 360px; height: 600px; }
  .front-layout {
    position: absolute; width: 600px; height: 360px;
    left: 0; top: 600px;
    transform-origin: 0 0; transform: rotate(-90deg);
  }
  .logo-frame {
    position: absolute; left: 30px; top: 28px; width: 540px; height: 222px;
    border: 6px solid var(--cork); background: var(--card-black);
  }
  .mascot-art {
    position: absolute; left: 0; top: 0; width: 150px; height: 210px;
    background: linear-gradient(160deg, var(--cork-light), var(--cork) 55%, var(--cork-dark));
  }
  .burger-art {
    position: absolute; left: 172px; top: 14px; width: 150px; height: 34px;
    border-radius: 6px;
    background: linear-gradient(180deg, var(--burger-top), var(--burger-mid) 45%, var(--burger-low) 80%, var(--cork-dark));
  }
  .brand-name {
    position: absolute; left: 172px; top: 62px; width: 356px;
    font-family: "Open Sans", sans-serif; font-weight: 800;
    color: var(--cork); font-size: 40px; line-height: 1; white-space: nowrap;
  }
  .brand-web {
    position: absolute; left: 172px; top: 150px; width: 356px;
    font-family: "Open Sans", sans-serif; font-weight: 800;
    color: var(--cork); font-size: 17px; letter-spacing: 0.5px; white-space: nowrap;
  }
  .tagline {
    position: absolute; left: 30px; top: 270px; width: 540px;
    font-family: "Tinos", "Times New Roman", serif; font-weight: 700;
    color: var(--white); font-size: 20px; line-height: 1.45; text-align: right;
  }

  /* Back card: landscape */
  .card--back { width: 600px; height: 360px; }
  .back-name {
    position: absolute; left: 0; right: 0; top: 62px; text-align: center;
    font-family: "Open Sans", sans-serif; font-weight: 800;
    color: var(--brand-red); font-size: 50px; line-height: 1;
  }
  .back-details {
    position: absolute; left: 0; right: 0; top: 175px; text-align: center;
  }
  .cab-line {
    font-family: "Tinos", "Times New Roman", serif;
    color: var(--cab-yellow); font-size: 17px; margin-bottom: 14px;
  }
  .hours-line {
    font-family: "Tinos", "Times New Roman", serif;
    color: var(--muted); font-size: 17px; margin-bottom: 22px;
  }
  .address-line {
    font-family: "Open Sans", sans-serif; font-weight: 700;
    color: var(--white); font-size: 17px; letter-spacing: 0.3px;
  }
</style>
</head>
<body>
<main class="stage">
  <section class="card card--front" aria-label="Business card front">
    <div class="front-layout">
      <div class="logo-frame">
        <div class="mascot-art" role="img" aria-label="Illustration of the bar's mascot in cork texture"></div>
        <div class="burger-art" role="img" aria-label="Photo of a stacked burger"></div>
        <div class="brand-name">TOMMO Larkdale</div>
        <div class="brand-web">TOMMOLARKDALE.EXAMPLE</div>
      </div>
      <p class="tagline">"No Fuss.<br>Just Games, Good Grub, Live Bands And Good Nights."</p>
    </div>
  </section>

  <section class="card card--back" aria-label="Business card back">
    <div class="back-name">TOMMO Larkdale</div>
    <div class="back-details">
      <p class="cab-line">Metro Cab: (555) 014-2288</p>
      <p class="hours-line">Open Daily: Mon-Fri: 11am - 2 am / Sat-Sun: 8am - 2 am</p>
      <p class="address-line">418 N. Campus Way, Larkdale, CA 90017 | 555.013.7261</p>
    </div>
  </section>
</main>
</body>
</html>
```